I need a header for the web site www.harlowspipeworks.example/demo
It must include the following
Existig Logo (I will upload the .png)
Text: Serving Calgary and Surrounding Areas for Over 30 Years!
24 Hour Service
Call 403.718.2946 (Note this isn't the actual phone number I will need to be able to change the Phone number once the site is ready to put in a tracking number so I am hoping I get a PSD file with this where the text is editable)
We wnat the feel to be warm and geared more towards a residential customer rather than an industial customer.
We would like blue tones but are open to anything warm.

Size: Aprroximately 960x300

• Rounded Corners to match the content area on the site

```html
<!DOCTYPE html>
<html lang="en">
<head>
<meta charset="utf-8">
<title>Harlow's Pipeworks</title>
<link rel="stylesheet" href="https://fonts.googleapis.com/css2?family=Open+Sans:ital,wght@0,400;0,600;0,700;1,400&family=Kreon:wght@300;400&family=Noto+Serif:ital@1&family=Arimo:ital,wght@0,400;0,700;1,700&display=swap">
<style>
  :root {
    --page-bg: #7f9ca4;
    --topbar: #2d4c61;
    --topbar-edge: #23394a;
    --panel: #ffffff;
    --panel-soft: #f3f3f1;
    --rule: #e2e2e2;
    --ink: #333333;
    --brand-blue: #4f7f9f;
    --phone-grey: #7b7b7b;
    --service-blue: #2f5068;
    --brace: #b8b8b8;
    --caption-bg: rgba(70, 70, 72, 0.82);
    --caption-text: #d6d6d6;
    --read-more: #e8c77a;
  }
  * { box-sizing: border-box; margin: 0; padding: 0; }
  html, body { width: 1200px; height: 768px; overflow: hidden; }
  body {
    position: relative;
    background: var(--page-bg);
    font-family: "Open Sans", Arial, sans-serif;
    color: var(--ink);
  }
  .topbar {
    position: absolute; left: 0; top: 0; width: 1200px; height: 48px;
    background: linear-gradient(#345a72, var(--topbar));
    border-bottom: 1px solid var(--topbar-edge);
  }
  .topbar-stitch {
    position: absolute; left: 0; top: 55px; width: 1200px;
    border-top: 1px dashed rgba(255,255,255,0.55);
  }
  .site-search {
    position: absolute; left: 857px; top: 12px; width: 166px; height: 26px;
    border-radius: 5px; background: #274256;
    box-shadow: inset 0 1px 3px rgba(0,0,0,0.5), 0 1px 0 rgba(255,255,255,0.12);
    font-size: 11px; color: #8aa1b0; padding: 6px 14px;
  }
  .site-search svg { position: absolute; right: 12px; top: 7px; }

  .brand-header {
    position: absolute; left: 113px; top: 79px; width: 958px; height: 122px;
    border-radius: 8px; border: 1px solid #d9d9d6;
    background: radial-gradient(ellipse at 45% 40%, #ffffff 0%, #f1efec 55%, #e3e1dd 100%);
  }
  .brand-name {
    position: absolute; left: 84px; top: 20px;
    font-family: "Arimo", Arial, sans-serif; font-size: 22px; letter-spacing: 2px;
    color: var(--service-blue); font-weight: 400;
  }
  .brand-mark {
    position: absolute; left: 62px; top: 27px; width: 12px; height: 12px;
    background: var(--brand-blue);
  }
  .tagline {
    position: absolute; left: 403px; top: 22px; width: 258px; height: 80px;
    text-align: center; font-family: "Arimo", Arial, sans-serif; line-height: 1;
  }
  .tagline svg { position: absolute; top: 2px; }
  .tagline .line-1 { position: absolute; left: 0; right: 0; top: 4px; font-size: 19px; font-weight: 700; color: var(--brand-blue); }
  .tagline .line-2 { position: absolute; left: 0; right: 0; top: 29px; font-size: 18px; color: #1f1f1f; }
  .tagline .line-3 { position: absolute; left: 0; right: 0; top: 50px; font-size: 24px; font-weight: 700; color: var(--brand-blue); }
  .call {
    position: absolute; right: 22px; top: 40px; text-align: right;
    font-family: "Arimo", Arial, sans-serif; line-height: 1;
  }
  .call .phone { font-size: 31px; font-weight: 700; font-style: italic; color: var(--phone-grey); }
  .call .hours { font-size: 18px; color: var(--service-blue); margin-top: 3px; }

  .main-nav {
    position: absolute; left: 113px; top: 216px; width: 958px; height: 57px;
    background: var(--panel); border-radius: 8px 8px 0 0;
    border-bottom: 1px solid var(--rule);
  }
  .main-nav ul { list-style: none; display: flex; padding-left: 29px; height: 100%; }
  .main-nav li {
    font-size: 12.5px; font-weight: 700; text-transform: uppercase; letter-spacing: 0.2px;
    padding: 0 17px; line-height: 57px; border-right: 1px solid var(--rule);
  }

  .slider {
    position: absolute; left: 113px; top: 281px; width: 958px; height: 340px;
    overflow: hidden;
  }
  .slide-photo {
    position: absolute; inset: 0;
    background: linear-gradient(100deg, #6a5340 0%, #8a7a6c 25%, #d9d9d6 40%, #c9c6c1 55%, #7a6a5a 75%, #5d4532 100%);
  }
  .slide-caption {
    position: absolute; left: 509px; top: 40px; width: 397px; height: 262px;
    background: var(--caption-bg); border-radius: 8px; padding: 28px 32px;
  }
  .slide-meta { font-family: "Noto Serif", Georgia, serif; font-style: italic; font-size: 12px; color: #9a9a9a; }
  .slide-meta b { color: #fff; font-weight: 400; }
  .slide-title { font-family: "Kreon", Georgia, serif; font-weight: 300; font-size: 30px; color: #fff; margin: 4px 0 6px; }
  .slide-text { font-size: 12px; line-height: 19px; color: var(--caption-text); }
  .read-more {
    position: absolute; right: 0; bottom: 0; padding: 6px 17px 7px;
    background: rgba(40,40,40,0.85); border-radius: 8px 0 8px 0;
    font-size: 12px; color: var(--read-more);
  }
  .slider-arrow {
    position: absolute; top: 427px; width: 33px; height: 67px;
    background: #fdfdfd; box-shadow: 0 0 4px rgba(0,0,0,0.25);
  }
  .slider-arrow.prev { left: 80px; border-radius: 34px 0 0 34px; }
  .slider-arrow.next { left: 1071px; border-radius: 0 34px 34px 0; }
  .slider-arrow svg { position: absolute; top: 27px; }
  .slider-arrow.prev svg { left: 13px; }
  .slider-arrow.next svg { left: 9px; }

  .thumb-strip {
    position: absolute; left: 113px; top: 621px; width: 958px; height: 103px;
    background: var(--panel);
  }
  .thumb-pointer {
    position: absolute; left: 60px; top: -10px; width: 0; height: 0;
    border-left: 10px solid transparent; border-right: 10px solid transparent;
    border-bottom: 10px solid var(--panel);
  }
  .thumb {
    position: absolute; top: 20px; width: 95px; height: 54px;
    border: 1px solid #cfcfcf;
  }
  .thumb.active { box-shadow: 0 0 6px rgba(0,0,0,0.6); }

  .section-bar {
    position: absolute; left: 113px; top: 724px; width: 958px; height: 44px;
    background: var(--panel-soft); border-top: 1px solid var(--rule);
  }
  .section-bar h2 {
    position: absolute; top: 13px; font-size: 12px; font-weight: 700;
    letter-spacing: -0.3px; text-transform: uppercase; color: #2a2a2a;
  }
  .section-bar .divider { position: absolute; left: 634px; top: 0; bottom: 0; border-left: 1px solid var(--rule); }
</style>
</head>
<body>
  <div class="topbar">
    <div class="site-search">search this site...
      <svg width="12" height="12" viewBox="0 0 12 12"><circle cx="7" cy="5" r="3.6" fill="none" stroke="#0e1b24" stroke-width="1.8"/><line x1="4.3" y1="7.7" x2="1" y2="11" stroke="#0e1b24" stroke-width="2"/></svg>
    </div>
  </div>
  <div class="topbar-stitch"></div>

  <header class="brand-header">
    <span class="brand-mark"></span>
    <div class="brand-name">HARLOW'S PIPEWORKS</div>
    <div class="tagline">
      <svg style="left:0" width="16" height="76" viewBox="0 0 16 76"><path d="M14 2 C4 2 8 34 2 38 C8 42 4 74 14 74" fill="none" stroke="var(--brace)" stroke-width="3"/></svg>
      <svg style="right:0" width="16" height="76" viewBox="0 0 16 76"><path d="M2 2 C12 2 8 34 14 38 C8 42 12 74 2 74" fill="none" stroke="var(--brace)" stroke-width="3"/></svg>
      <div class="line-1">Serving Calgary</div>
      <div class="line-2">and Surrounding Areas for</div>
      <div class="line-3">Over 30 Years!</div>
    </div>
    <div class="call">
      <div class="phone">Call 403-718-2946</div>
      <div class="hours">24 Hour Service</div>
    </div>
  </header>

  <nav class="main-nav">
    <ul>
      <li>Home</li>
      <li>Services »</li>
      <li>Product Reviews</li>
      <li>Links</li>
      <li>Articles</li>
      <li>Contact Us</li>
      <li>About Us</li>
      <li>Employee Login</li>
    </ul>
  </nav>

  <section class="slider">
    <div class="slide-photo" role="img" aria-label="Freestanding white bathtub in a renovated bathroom with wooden cabinets and stone wall"></div>
    <div class="slide-caption">
      <p class="slide-meta">Posted by <b>admin</b> on Sep 15, 2010</p>
      <h1 class="slide-title">Residential Plumbing</h1>
      <p class="slide-text">Quisque ullamcorper enim vel tellus rhoncus et fermentum diam congue. Phasellus eu turpis lorem, id gravida nunc. In bibendum nulla vel quam pretium a fringilla erat ornare. Etiam hendrerit quam sed orci congue posuere laoreet urna condimentum. Nam vestibulum gravida semper. Maecenas ac nunc purus, et aliquam urna. Curabitur quis tellus vitae dolor tristique egestas. Fusce metus sem, accumsan vel auctor...</p>
      <span class="read-more">Read More</span>
    </div>
  </section>
  <div class="slider-arrow prev"><svg width="10" height="14" viewBox="0 0 10 14"><path d="M8 1 L2 7 L8 13" fill="none" stroke="#8a8a8a" stroke-width="2.5"/></svg></div>
  <div class="slider-arrow next"><svg width="10" height="14" viewBox="0 0 10 14"><path d="M2 1 L8 7 L2 13" fill="none" stroke="#8a8a8a" stroke-width="2.5"/></svg></div>

  <div class="thumb-strip">
    <span class="thumb-pointer"></span>
    <div class="thumb active" style="left:24px;background:linear-gradient(#6b5644,#d8d6d2 50%,#5a4a3a)" role="img" aria-label="White bathtub"></div>
    <div class="thumb" style="left:140px;background:linear-gradient(135deg,#8a4a2a,#c07a55,#6a3a22)" role="img" aria-label="In-floor heating pipes"></div>
    <div class="thumb" style="left:256px;background:linear-gradient(90deg,#4a5058,#c8c8c4,#6b6f74)" role="img" aria-label="Water heaters in a utility room"></div>
    <div class="thumb" style="left:372px;background:linear-gradient(90deg,#6a5a4a,#b8b0a2,#7a6a58)" role="img" aria-label="Boiler piping installation"></div>
    <div class="thumb" style="left:488px;background:linear-gradient(#5a4030,#a8a49a 60%,#3a3a2e)" role="img" aria-label="Glass vessel sink"></div>
    <div class="thumb" style="left:604px;background:linear-gradient(#dcdad4,#3a3a3a 60%,#d8d4cc)" role="img" aria-label="Dark stone bathtub"></div>
    <div class="thumb" style="left:720px;background:linear-gradient(#5a3a28,#c8b8a4 60%,#4a2e20)" role="img" aria-label="Jetted tub under windows"></div>
    <div class="thumb" style="left:836px;background:linear-gradient(90deg,#3a6ab0,#6aa0d8,#c8c8c8)" role="img" aria-label="Commercial boiler equipment"></div>
  </div>

  <div class="section-bar">
    <h2 style="left:256px">Most Recent Articles</h2>
    <span class="divider"></span>
    <h2 style="left:735px">Harlow's Pipeworks</h2>
  </div>
</body>
</html>
```